I make small projects usually ranging from cutting boards, kitchen utensils , cedar gardens projects, basically anything I can fit in a 2 car garage workshop. I've been ask by numerous people if I have website or a facebook page or something where they go look at my products/abilities. I pretty much make anything anyone wants out of wood and can customize to their needs.

R.T.Belcourt Custom Woodworks Inc. is my business name.

At this time I'm currently seeking a branding logo and business card set for my new business. I'm based out of the city of Edmonton, Alberta, Canada. My target market would be Middle class to upper class, new home-owners who like quality products to compliment the look of their new homes and property at decent prices. Although this my current work practice I am thinking I venture into finish carpentry long term and that is why I choose the name to be more formal. However I would the design to different that just a plain card. Would like to incorporate wood grain color or pattern. I would like a slogan or logo text, but I have no idea what ill leave that up to you and see what you come back with.

Target Market(s)

My target market would be Middle class to upper class, new home-owners who like quality products to compliment the look of their new homes and property at decent prices.

Industry/Entity Type

Carpentry

Contact Information for Business Card

Rowan T. Belcourt
Craftsmen

R.T.Belcourt Custom Woodworks Inc
Address: 2817 Thornbury Way SW, Edmonton, A.B., T5K 2P8
Cell: (780) 555-0193
Smtp: rtbwoodworks@examplemail.net
Website: XXXXXXX yet to be determined
Facebook: R.T.Belcourt Custom Woodworks Inc.

Logo styles of interest
Emblem Logo
Pictorial/Combination Logo
Abstract Logo
Lettermark Logo
Requirements
Nice to have
• Although there is a allot information in the business card detail area, feel free to alter as you see fir. example: remove business address, website(as i dont have one yet)

```html
<!DOCTYPE html>
<html lang="en">
<head>
<meta charset="utf-8">
<title>R.T.Belcourt Custom Woodworks Inc. – Business Card</title>
<link rel="stylesheet" href="https://fonts.googleapis.com/css2?family=Marcellus&family=Open+Sans:wght@600;700&display=swap">
<style>
  :root {
    --wood-dark: #5e220a;
    --wood-mid: #9a4415;
    --wood-light: #c0621f;
    --ink-brown: #3a1206;
    --paper: #ffffff;
    --rule-grey: #9a9a9a;
    --contact-white: #ffffff;
  }
  * { margin: 0; padding: 0; box-sizing: border-box; }
  html, body {
    width: 1200px;
    height: 667px;
    overflow: hidden;
    background: var(--paper);
  }
  .card {
    position: relative;
    width: 1200px;
    height: 667px;
    overflow: hidden;
  }
  .wood-band {
    position: absolute;
    left: 0;
    width: 1200px;
    background:
      radial-gradient(ellipse 60% 80% at 30% 40%, rgba(192, 98, 31, 0.55), transparent 70%),
      radial-gradient(ellipse 50% 70% at 80% 60%, rgba(94, 34, 10, 0.45), transparent 70%),
      linear-gradient(170deg, var(--wood-mid) 0%, var(--wood-light) 35%, var(--wood-mid) 60%, var(--wood-dark) 100%);
  }
  .wood-band--top { top: 0; height: 155px; }
  .wood-band--bottom { top: 500px; height: 167px; }

  .name-strip {
    position: absolute;
    top: 155px;
    left: 0;
    width: 1200px;
    height: 345px;
    background: var(--paper);
    border-top: 1px solid var(--rule-grey);
    border-bottom: 1px solid var(--rule-grey);
  }
  .brand-mark {
    position: absolute;
    left: 45px;
    top: 78px;
    width: 173px;
    height: 173px;
  }
  .brand-tagline {
    position: absolute;
    left: 45px;
    top: 290px;
    font-family: "Open Sans", sans-serif;
    font-weight: 600;
    font-size: 13.5px;
    color: var(--ink-brown);
    letter-spacing: -0.1px;
  }
  .brand-name {
    position: absolute;
    left: 245px;
    top: 56px;
    width: 925px;
    height: 220px;
    display: flex;
    align-items: center;
    justify-content: center;
    font-family: "Marcellus", serif;
    font-size: 148px;
    line-height: 1;
    color: var(--ink-brown);
    letter-spacing: 2px;
  }

  .contact-line {
    position: absolute;
    top: 575px;
    left: 0;
    width: 1200px;
    text-align: center;
    font-family: "Open Sans", sans-serif;
    font-weight: 700;
    font-size: 28px;
    color: var(--contact-white);
    white-space: nowrap;
  }
  .contact-line .sep {
    display: inline-block;
    margin: 0 14px;
  }
</style>
</head>
<body>
  <main class="card">
    <div class="wood-band wood-band--top" role="img" aria-label="Reddish-brown polished wood grain texture"></div>

    <section class="name-strip">
      <svg class="brand-mark" viewBox="0 0 173 173" aria-hidden="true">
        <rect x="4" y="4" width="165" height="165" fill="none" stroke="var(--ink-brown)" stroke-width="7"/>
      </svg>
      <p class="brand-tagline">Custom Woodworks Inc.</p>
      <h1 class="brand-name">BELCOURT</h1>
    </section>

    <div class="wood-band wood-band--bottom" role="img" aria-label="Reddish-brown polished wood grain texture"></div>

    <p class="contact-line">
      <span class="contact-web">www.rtbwood.net</span><span class="sep">•</span><span class="contact-mail">e-mail: info@rtbwood.net</span><span class="sep">•</span><span class="contact-tel">tel: +1 555 01 93</span>
    </p>
  </main>
</body>
</html>
```